Business Card Design Project

We need a business card design for a new company based in Singapore called 'Bright Ladder Pte Ltd'. We provide personal development training and emotional intelligence workshops. Our slogan is "Actualize your potentials". We will not have a company address on the business card. Only phone number, email address and website address.

Target Market(s)

Adults age 25 to 45 years old.
Mostly working in a job.

Industry/Entity Type

Training

Colors
0255a2
f37123

```html
<!DOCTYPE html>
<html lang="en">
<head>
<meta charset="utf-8">
<title>Bright Ladder Pte Ltd – Business Card</title>
<link href="https://fonts.googleapis.com/css2?family=Montserrat:wght@400;700&family=Open+Sans:wght@400;600&display=swap" rel="stylesheet">
<style>
  :root {
    --brand-blue: #0255a2;
    --brand-navy: #1d3f7a;
    --brand-orange: #f37123;
    --ink: #2b2b2b;
    --muted: #8a96a8;
    --paper: #ffffff;
    --backdrop: #e9e6e1;
  }
  * { box-sizing: border-box; margin: 0; padding: 0; }
  html, body { width: 1200px; height: 1023px; overflow: hidden; }
  body {
    background: var(--backdrop);
    font-family: "Open Sans", Arial, sans-serif;
    display: flex;
    flex-direction: column;
    align-items: center;
    justify-content: center;
    gap: 50px;
  }
  .card {
    width: 760px;
    height: 434px;
    position: relative;
    overflow: hidden;
    border-radius: 4px;
    box-shadow: 0 10px 28px rgba(0,0,0,.18);
  }

  /* Front */
  .card-front { background: var(--paper); }
  .front-emblem {
    position: absolute;
    left: -60px;
    bottom: -110px;
    width: 400px;
    height: 400px;
    border-radius: 50%;
    background: radial-gradient(circle at 55% 40%, rgba(243,113,35,.35) 0 18%, rgba(2,85,162,.25) 40%, rgba(2,85,162,.08) 70%, transparent 71%);
  }
  .front-brand {
    position: absolute;
    left: 330px;
    top: 58px;
  }
  .brand-name {
    font-family: "Montserrat", Arial, sans-serif;
    font-weight: 700;
    font-size: 44px;
    letter-spacing: -1px;
    color: var(--brand-blue);
    line-height: 1;
  }
  .brand-suffix {
    display: flex;
    align-items: center;
    gap: 12px;
    margin-top: 6px;
    font-family: "Montserrat", Arial, sans-serif;
    font-size: 20px;
    letter-spacing: 4px;
    color: var(--muted);
  }
  .brand-suffix::before {
    content: "";
    width: 150px;
    height: 1px;
    background: var(--muted);
  }
  .front-roles {
    position: absolute;
    left: 330px;
    top: 160px;
    font-size: 13px;
    letter-spacing: 1px;
    color: var(--ink);
  }
  .person {
    position: absolute;
    left: 330px;
    top: 212px;
    font-family: "Montserrat", Arial, sans-serif;
    font-weight: 700;
    font-size: 20px;
    letter-spacing: 1px;
    color: var(--brand-blue);
  }
  .person-title {
    position: absolute;
    left: 330px;
    top: 240px;
    font-size: 12px;
    letter-spacing: 1.5px;
    color: var(--muted);
  }
  .front-divider {
    position: absolute;
    left: 330px;
    top: 272px;
    width: 380px;
    height: 2px;
    background: var(--brand-orange);
  }
  .contact-list {
    position: absolute;
    left: 330px;
    top: 296px;
    list-style: none;
    display: flex;
    flex-direction: column;
    gap: 10px;
    font-size: 16px;
    color: var(--ink);
  }
  .contact-list li { display: flex; align-items: center; gap: 12px; }
  .contact-icon { width: 20px; height: 20px; flex: none; }

  /* Back */
  .card-back {
    background: linear-gradient(135deg, #2a5aa3 0%, var(--brand-navy) 55%, #17325f 100%);
  }
  .back-emblem {
    position: absolute;
    left: 170px;
    top: -120px;
    width: 520px;
    height: 520px;
    border-radius: 50%;
    background: radial-gradient(circle, rgba(255,255,255,.08) 0 55%, rgba(255,255,255,.03) 56% 70%, transparent 71%);
  }
  .back-lockup {
    position: absolute;
    left: 50%;
    top: 50%;
    transform: translate(-50%, -50%);
    display: flex;
    align-items: center;
    gap: 18px;
  }
  .back-mark {
    width: 64px;
    height: 64px;
    border-radius: 50%;
    background: var(--brand-orange);
    flex: none;
  }
  .back-lockup .brand-name { color: var(--paper); font-size: 48px; }
  .back-lockup .brand-suffix { color: #c9d6ea; }
  .back-lockup .brand-suffix::before { background: #c9d6ea; }
</style>
</head>
<body>

  <section class="card card-front" aria-label="Business card front">
    <div class="front-emblem" role="img" aria-label="Large decorative brand emblem in blue and orange"></div>

    <div class="front-brand">
      <div class="brand-name">Bright Ladder</div>
      <div class="brand-suffix">PTE LTD</div>
    </div>

    <p class="front-roles">COACH | TRAINER | MASTER FACILITATOR</p>

    <p class="person">MARCUS TAN</p>
    <p class="person-title">FOUNDER</p>
    <div class="front-divider"></div>

    <ul class="contact-list">
      <li>
        <svg class="contact-icon" viewBox="0 0 20 20" aria-hidden="true">
          <circle cx="10" cy="10" r="10" fill="var(--brand-orange)"/>
          <path d="M7 5.5l2 2-1 1.3a6 6 0 0 0 3.2 3.2l1.3-1 2 2-1.2 1.5C9.8 14.3 5.7 10.2 5.5 6.7z" fill="#fff"/>
        </svg>
        0412558730
      </li>
      <li>
        <svg class="contact-icon" viewBox="0 0 20 20" aria-hidden="true">
          <circle cx="10" cy="10" r="10" fill="var(--brand-orange)"/>
          <rect x="5" y="6.5" width="10" height="7" fill="none" stroke="#fff" stroke-width="1.3"/>
          <path d="M5 6.5l5 4 5-4" fill="none" stroke="#fff" stroke-width="1.3"/>
        </svg>
        marcus@brightladder.com
      </li>
      <li>
        <svg class="contact-icon" viewBox="0 0 20 20" aria-hidden="true">
          <circle cx="10" cy="10" r="10" fill="var(--brand-orange)"/>
          <circle cx="10" cy="10" r="5" fill="none" stroke="#fff" stroke-width="1.2"/>
          <ellipse cx="10" cy="10" rx="2.2" ry="5" fill="none" stroke="#fff" stroke-width="1.1"/>
          <path d="M5 10h10" stroke="#fff" stroke-width="1.1"/>
        </svg>
        www.brightladder.com
      </li>
    </ul>
  </section>

  <section class="card card-back" aria-label="Business card back">
    <div class="back-emblem" role="img" aria-label="Faint large brand emblem decoration"></div>
    <div class="back-lockup">
      <span class="back-mark" aria-hidden="true"></span>
      <div>
        <div class="brand-name">Bright Ladder</div>
        <div class="brand-suffix">PTE LTD</div>
      </div>
    </div>
  </section>

</body>
</html>
```